Corvane Aviation - Flight school needs help!

I need help creating a sign for a new flight school. I am looking for something that is exciting, energetic, and magnetizing. The sign should make you feel compelled to come in and see what the flight school offers. I hope that the sign can also make the customer's/clients feel like they are entering more than just a business, something bigger than themselves. If there is some way to make the potential customer/client daydream about flying, or just excited to see our logo, that would be amazing.
This sign will be going up on the side of a metal building.

Industry/Entity Type

Aviation

Requirements
Must have
• Must list what we offer which includes:
Aircraft Rentals
Flight Training
Ground School

Must have our email address which is:
info@corvaneaviation.example

Must have our phone number which is:
205-731-0862
Nice to have
• Energizing, exciting, and magnetizing. Something that draws you in and excites you about the possibilities of learning to fly or renting an airplane from the flight school.

I have attached a picture of one of the airplanes as an example, I have also attached multiple logos.

```html
<!DOCTYPE html>
<html lang="en">
<head>
<meta charset="utf-8">
<title>Corvane Aviation – Sign</title>
<link rel="stylesheet" href="https://fonts.googleapis.com/css2?family=Saira:wght@400;500;600;700&display=swap">
<style>
  :root {
    --navy: #0e2262;
    --navy-deep: #08173f;
    --navy-light: #1d3a8a;
    --aerial-a: #2b4a96;
    --aerial-b: #3a5aa6;
    --red: #ee1c24;
    --white: #ffffff;
    --backdrop: #d9d9d9;
    --hangar-beam: #9c6b4e;
    --hangar-wall: #cfc6b6;
    --hangar-wall-light: #e3ddd2;
    --floor: #d3dde4;
    --floor-light: #e6ecef;
    --plane-white: #eef1f4;
  }
  html, body {
    margin: 0;
    padding: 0;
    width: 1200px;
    height: 1200px;
    overflow: hidden;
    background: var(--backdrop);
    font-family: "Saira", "Arial", sans-serif;
  }
  .sign {
    position: absolute;
    left: 16px;
    top: 308px;
    width: 1168px;
    height: 584px;
    overflow: hidden;
    background: linear-gradient(160deg, var(--navy) 0%, var(--navy-deep) 100%);
    box-shadow: 0 6px 18px rgba(0,0,0,0.25);
  }
  .sign__art {
    position: absolute;
    inset: 0;
    width: 1168px;
    height: 584px;
  }
  .offer-band {
    position: absolute;
    left: 0;
    top: 51px;
    width: 313px;
    height: 46px;
    background: var(--red);
    clip-path: polygon(0 0, 100% 0, 88% 100%, 0 100%);
  }
  .offer-band__label {
    position: absolute;
    left: 48px;
    top: 0;
    line-height: 46px;
    font-size: 33px;
    font-weight: 600;
    color: var(--white);
  }
  .services {
    position: absolute;
    left: 48px;
    top: 122px;
    margin: 0;
    padding: 0;
    list-style: none;
  }
  .service {
    position: relative;
    padding-left: 32px;
    margin-bottom: 38px;
    color: var(--white);
  }
  .service::before {
    content: "";
    position: absolute;
    left: 0;
    top: 20px;
    width: 15px;
    height: 15px;
    background: var(--red);
  }
  .service__main {
    display: block;
    font-size: 57px;
    line-height: 56px;
    font-weight: 500;
    letter-spacing: -1.5px;
  }
  .service__sub {
    display: block;
    margin-top: -2px;
    font-size: 31px;
    line-height: 32px;
    font-weight: 700;
    letter-spacing: 14px;
  }
  .contact {
    position: absolute;
    left: 46px;
    top: 478px;
    color: var(--white);
  }
  .contact__phone {
    display: flex;
    align-items: center;
    gap: 12px;
    font-size: 60px;
    line-height: 58px;
    font-weight: 500;
    letter-spacing: 0.5px;
  }
  .contact__icon { width: 44px; height: 44px; }
  .contact__email {
    margin-top: 2px;
    font-size: 21px;
    font-weight: 400;
    letter-spacing: 3.6px;
  }
  .brand {
    position: absolute;
    left: 368px;
    top: 165px;
    width: 250px;
    height: 250px;
    border-radius: 50%;
    background: var(--white);
    display: flex;
    align-items: center;
    justify-content: center;
    text-align: center;
  }
  .brand__name {
    font-size: 34px;
    line-height: 38px;
    font-weight: 700;
    color: var(--navy);
    letter-spacing: 1px;
  }
</style>
</head>
<body>
  <section class="sign">
    <svg class="sign__art" viewBox="0 0 1168 584" xmlns="http://www.w3.org/2000/svg">
      <defs>
        <radialGradient id="aerial-texture" cx="0.35" cy="0.35" r="0.7">
          <stop offset="0" stop-color="var(--aerial-b)" stop-opacity="0.55"/>
          <stop offset="0.5" stop-color="var(--aerial-a)" stop-opacity="0.3"/>
          <stop offset="1" stop-color="var(--navy-deep)" stop-opacity="0"/>
        </radialGradient>
        <linearGradient id="hangar-photo" x1="0" y1="0" x2="0" y2="1">
          <stop offset="0" stop-color="var(--hangar-beam)"/>
          <stop offset="0.08" stop-color="var(--hangar-wall)"/>
          <stop offset="0.4" stop-color="var(--hangar-wall-light)"/>
          <stop offset="0.62" stop-color="var(--plane-white)"/>
          <stop offset="0.78" stop-color="var(--floor)"/>
          <stop offset="1" stop-color="var(--floor-light)"/>
        </linearGradient>
      </defs>
      <rect class="aerial-texture" role="img" aria-label="Faint aerial view of an airfield behind the service list"
            x="0" y="0" width="760" height="584" fill="url(#aerial-texture)"/>
      <path class="photo-frame" d="M700 0 C575 60 497 180 507 310 C517 430 597 540 707 584 L1168 584 L1168 0 Z" fill="var(--white)"/>
      <path class="photo-area" role="img" aria-label="Photo of a white and navy single-engine training airplane parked in a hangar"
            d="M718 0 C593 60 518 180 528 310 C538 430 618 540 726 584 L1168 584 L1168 0 Z" fill="url(#hangar-photo)"/>
    </svg>

    <div class="offer-band"><span class="offer-band__label">WE OFFER</span></div>

    <ul class="services">
      <li class="service"><span class="service__main">AIRCRAFT</span><span class="service__sub">RENTALS</span></li>
      <li class="service"><span class="service__main">FLIGHT</span><span class="service__sub">TRAINING</span></li>
      <li class="service"><span class="service__main">GROUND</span><span class="service__sub">SCHOOL</span></li>
    </ul>

    <div class="contact">
      <div class="contact__phone">
        <svg class="contact__icon" viewBox="0 0 24 24" aria-hidden="true">
          <path fill="var(--red)" d="M6.6 10.8c1.4 2.8 3.8 5.1 6.6 6.6l2.2-2.2c.3-.3.7-.4 1-.2 1.1.4 2.3.6 3.6.6.6 0 1 .4 1 1V20c0 .6-.4 1-1 1C10.6 21 3 13.4 3 4c0-.6.4-1 1-1h3.5c.6 0 1 .4 1 1 0 1.3.2 2.5.6 3.6.1.3 0 .7-.2 1l-2.3 2.2z"/>
          <path fill="none" stroke="var(--red)" stroke-width="1.4" stroke-linecap="round" d="M14 3.5a6.5 6.5 0 0 1 6.5 6.5M14 6.5a3.5 3.5 0 0 1 3.5 3.5"/>
        </svg>
        <span>205-731-0862</span>
      </div>
      <div class="contact__email">INFO@CORVANEAVIATION.EXAMPLE</div>
    </div>

    <div class="brand"><span class="brand__name">CORVANE<br>AVIATION</span></div>
  </section>
</body>
</html>
```